A billboard for Harlow Ridge Construction size 36.5’ x 14.5’

Hi guys. We are purchasing a billboard and are looking for a design (size 36.5’ x 14.5’). Our slogan is "Quality you deserve, service you can count on". The goal of this billboard is brand recognition primarily letting people know we do roofs. Attached are logos that can be used if needed. Not necessarily all of them need to be used.

Target Market(s)

Residents in the local areas needing or thinking about a roof replacement

Industry/Entity Type

Roofing

Requirements
Must have
• Logo and services (roof replacement, gutters, siding, and snow removal)
Nice to have
• take a look at our website for ideas www.harlowridgeconstruction.example

```html
<!DOCTYPE html>
<html lang="en">
<head>
<meta charset="utf-8">
<title>Harlow Ridge Construction Billboard</title>
<link rel="stylesheet" href="https://fonts.googleapis.com/css2?family=Tinos&family=Poppins:wght@700;800&display=swap">
<style>
  :root {
    --page: #ffffff;
    --board: #000000;
    --ink-light: #ffffff;
    --ink-dark: #0a0a0a;
    --accent-red: #d8261c;
    --roof-brown: #7a6a52;
    --wood-tan: #b07a45;
  }
  html, body {
    margin: 0;
    padding: 0;
    width: 1200px;
    height: 1200px;
    overflow: hidden;
    background: var(--page);
  }
  .billboard-canvas {
    display: block;
    width: 1200px;
    height: 1200px;
  }
  .brand-name {
    font-family: "Tinos", "Times New Roman", serif;
    fill: var(--ink-light);
  }
  .slogan {
    font-family: "Poppins", Arial, sans-serif;
    font-weight: 800;
    fill: var(--ink-dark);
    font-size: 24px;
  }
  .contact {
    font-family: "Poppins", Arial, sans-serif;
    font-weight: 700;
    fill: var(--ink-light);
    letter-spacing: 1px;
  }
</style>
</head>
<body>
<svg class="billboard-canvas" viewBox="0 0 1200 1200" xmlns="http://www.w3.org/2000/svg">
  <defs>
    <linearGradient id="roofTones" x1="0" y1="0" x2="1" y2="1">
      <stop offset="0" stop-color="#8a7b62"/>
      <stop offset="0.5" stop-color="var(--wood-tan)"/>
      <stop offset="1" stop-color="var(--roof-brown)"/>
    </linearGradient>
  </defs>

  <rect class="board" x="135" y="414" width="930" height="371" fill="var(--board)"/>

  <polygon class="hero-photo" role="img" aria-label="Photo of a house with shingled roofs, wooden gables and a stone chimney"
           points="152,433 388,433 528,600 388,767 152,767" fill="url(#roofTones)"/>
  <polyline class="photo-chevron" points="398,433 538,600 398,767" fill="none" stroke="var(--ink-light)" stroke-width="4"/>

  <text class="brand-name" x="468" y="516" font-size="92" textLength="560" lengthAdjust="spacingAndGlyphs">HarlowRidge</text>
  <text class="brand-name" x="540" y="595" font-size="80">Construction</text>

  <polygon class="slogan-band" points="576,617 1028,617 1028,697 508,697" fill="var(--accent-red)"/>
  <text class="slogan" x="578" y="647">QUALITY YOU DESERVE, SERVICE</text>
  <text class="slogan" x="557" y="684">YOU CAN COUNT ON…………</text>

  <text class="contact" x="770" y="726" font-size="22" text-anchor="middle" textLength="518" lengthAdjust="spacingAndGlyphs">www.harlowridgeconstruction.example</text>
  <text class="contact" x="768" y="766" font-size="25" text-anchor="middle">PH: 5550142783</text>
</svg>
</body>
</html>
```